Guaranteed Job - Sleek Sexy Business Card UV Spot

Im looking for a sleek and sexy business card, that resembles elite or VIP status status.
our business is corinvale.example
you can view our products on there, but our main audience for handing out our cards will be for people in the hospitality industry, so it will need to impress high management and CEO of hotels and restaurants, bars, clubs etc...
the card features will have UV spot on both sides, 400gsm stock. standard size.
Artwork should be 86 x 54mm + 2mm bleed = 90 x 58mm
it should have a nice "unique" uv spot pattern that highlights the card, not a repeated pattern, theres no originality there, and it will be disregarded.
The written material will be:
Corin Vale Hospitality College (logo)
Tobin Marsh
Director
Phone: 1300 615 737
Mobile: 0455 817 296
Email: info@corinvale.example
website: www.corinvale.example
I'm looking for originality here, i don't want just a simple stock card, want something that has a wow factor for people.
You will find the logo attached. you may invert the white to black words to suit the background as you please.
thank you and good luck
As a side note, ive received a lot of proposals, im too busy to give feedback to each and every one, so if i havent provided feedback for your design within 24 hours, then consider it not acceptable, and you could resubmit another design.
So far i have not seen any design that stood out for me, they all seem pretty generic. there nothing thats unique, i would figure for the amount that im offering, that people would put some more effort and creativity into the design.
so far over 200 designs submitted, and nothing i have seen looks very original, everything looks like a different variation of the same stuff, i said it very clearly i wanted something unique, the only thing that has come close to it so far is this one
Reason: Ive received alot of design concepts and i have reviewed everyone, but i havent had time to give feedback to every single one, only the ones that have interested me, if i havent responded, its because i havent found it good enough.
so far only a few design have been on par with what ive been looking for, an attractive eye popping design.
heres a few of them,
http://files.pixelbazaar.example/design_img/51736/62418/62418_2840915_51736_image.jpg
http://files.pixelbazaar.example/design_img/51736/68254/68254_2841377_51736_image.jpg
theyre, both unique and original, and eye catching, the only thing theyre missing is the sexyness.
if you still think you have some creativity left in your minds, then throw it on here.
Reason: Sorry guys for the delay, I was in a serious accident and out of commission for the past few months, I'm just slowly recovering now, please bare with me as i try to attend to this project, it may take me awhile as I have other projects that are on standby, I'm not 100% at the moment, so im extending the deadline for 2 weeks right now. Thanks for your patience.
Hospitality

```html
<!DOCTYPE html>
<html lang="en">
<head>
<meta charset="utf-8">
<title>Corin Vale Hospitality College – Business Card</title>
<link rel="stylesheet" href="https://fonts.googleapis.com/css2?family=Open+Sans:wght@400;600&display=swap">
<style>
  :root {
    --page-bg: #e6e8eb;
    --card-light: #e9f1f7;
    --card-mid: #cfdeea;
    --card-edge: #b3c9da;
    --navy: #1d3447;
    --brand-blue: #3d9fda;
    --bar-text: #ffffff;
    --drink-foam: #d8b57a;
    --drink-amber: #a5521f;
    --drink-dark: #4e140a;
  }
  * { box-sizing: border-box; margin: 0; padding: 0; }
  html, body { width: 1200px; height: 1000px; overflow: hidden; }
  body {
    background: var(--page-bg);
    font-family: "Open Sans", Arial, sans-serif;
    position: relative;
  }
  .card {
    position: absolute;
    left: 260px;
    width: 680px;
    height: 437px;
    overflow: hidden;
    background: radial-gradient(ellipse at 30% 35%, var(--card-light) 0%, var(--card-mid) 60%, var(--card-edge) 100%);
    box-shadow: 0 6px 18px rgba(0, 0, 0, 0.18);
  }
  .card--front { top: 43px; }
  .card--back { top: 523px; }

  .beverage-photo {
    position: absolute;
    left: 34px;
    top: 8px;
    width: 256px;
    height: 429px;
    border-radius: 90px 90px 0 0;
    background: linear-gradient(180deg, var(--drink-foam) 0%, var(--drink-amber) 28%, var(--drink-dark) 62%, #7a2412 100%);
  }

  .brand {
    position: absolute;
    left: 365px;
    top: 40px;
    display: flex;
    align-items: center;
    gap: 12px;
    color: var(--brand-blue);
    font-weight: 600;
  }
  .brand__mark {
    width: 40px;
    height: 40px;
    background: var(--brand-blue);
  }
  .brand__name {
    font-size: 26px;
    line-height: 1.05;
    text-transform: uppercase;
  }
  .brand__name small {
    display: block;
    font-size: 11.5px;
    letter-spacing: 0.5px;
  }

  .info-bar {
    position: absolute;
    height: 42px;
    background: var(--navy);
    color: var(--bar-text);
    font-size: 21px;
    display: flex;
    align-items: center;
    justify-content: flex-end;
    gap: 10px;
    padding-right: 18px;
    transform: rotate(-2deg);
    transform-origin: left center;
    box-shadow: 0 4px 6px rgba(0, 0, 0, 0.3);
  }
  .info-bar svg { width: 20px; height: 20px; fill: var(--bar-text); flex: none; }

  .bar-name { left: 270px; top: 173px; width: 209px; }
  .bar-role { left: 270px; top: 224px; width: 255px; }
  .bar-phone { left: 270px; top: 275px; width: 308px; }
  .bar-mobile { left: 270px; top: 326px; width: 359px; }

  .bar-back-name { left: 270px; top: 181px; width: 212px; }
  .bar-email { left: 286px; top: 232px; width: 343px; }
  .bar-web { left: 286px; top: 302px; width: 312px; }
</style>
</head>
<body>

<section class="card card--front" aria-label="Business card front">
  <div class="beverage-photo" role="img" aria-label="Photograph of a glass of cola with ice splashing over the rim"></div>
  <div class="brand">
    <span class="brand__mark"></span>
    <p class="brand__name">Corin Vale<small>Hospitality College</small></p>
  </div>
  <p class="info-bar bar-name">Tobin Marsh</p>
  <p class="info-bar bar-role">Director</p>
  <p class="info-bar bar-phone">
    <svg viewBox="0 0 20 20" aria-hidden="true"><path d="M2 6c0-2 3-3 8-3s8 1 8 3v2h-4V6.5c-1-.4-2.4-.6-4-.6s-3 .2-4 .6V8H2z"/><rect x="4" y="9" width="12" height="8" rx="1.5"/></svg>
    1300 615 737
  </p>
  <p class="info-bar bar-mobile">
    <svg viewBox="0 0 20 20" aria-hidden="true"><rect x="1" y="1" width="18" height="18" rx="3"/><path fill="#1d3447" d="M6 5l2 0 1 3-1.5 1c.7 1.5 1.8 2.6 3.3 3.3l1-1.5 3 1v2c0 .7-.5 1.2-1.2 1.2C8.5 15 5 11.5 4.8 6.2 4.8 5.5 5.3 5 6 5z"/></svg>
    0455 817 296
  </p>
</section>

<section class="card card--back" aria-label="Business card back">
  <div class="beverage-photo" role="img" aria-label="Photograph of a glass of cola with ice splashing over the rim"></div>
  <div class="brand">
    <span class="brand__mark"></span>
    <p class="brand__name">Corin Vale<small>Hospitality College</small></p>
  </div>
  <p class="info-bar bar-back-name">Tobin Marsh</p>
  <p class="info-bar bar-email">
    <svg viewBox="0 0 20 20" aria-hidden="true"><rect x="1" y="4" width="18" height="12"/><path fill="none" stroke="#1d3447" stroke-width="1.5" d="M1.5 4.5L10 11l8.5-6.5"/></svg>
    info@corinvale.example
  </p>
  <p class="info-bar bar-web">
    <svg viewBox="0 0 20 20" aria-hidden="true"><circle cx="10" cy="10" r="9"/><g fill="none" stroke="#1d3447" stroke-width="1.2"><ellipse cx="10" cy="10" rx="4" ry="9"/><path d="M1 10h18M2.5 5.5h15M2.5 14.5h15"/></g></svg>
    www.corinvale.example
  </p>
</section>

</body>
</html>
```